International IT business needs website revamp.

Velbric Limited would like their current website (www.velbriclimited.example) to be revamped/modernized to reflect up-to-date goods and services. Currently, Velbric is offering a conversational AI workflow platform for both enterprise clients and as a DIY solution for SMBs. This platform is called tmPilot and allows organizations to automate simple and repetitive workflows to drive their operational efficiency. In addition to the solution offering, Velbric Limited also provides professional IT services. With that said, please use www.velbriclimited.example and www.tmpilot.example for reference of current logos and colourways desired. Furthermore, refer to the attached PDF for a general idea of what to include in the site. The final design should be easy to navigate, clear, concise, and emphasize tmPilot as a solution for enterprise clients (while redirecting SMBs to the tmPilot website) looking to automate workflow processes/kickstart their digital transformation journey.
Updates
Coding
Number of Pages Required
5+ page
Font styles to use
Look and feel
Each slider illustrates characteristics of the customer's brand and the style your logo design should communicate.

```html
<!DOCTYPE html>
<html lang="en">
<head>
<meta charset="utf-8">
<title>Velbric Limited — Solutions</title>
<link rel="stylesheet" href="https://fonts.googleapis.com/css2?family=Lilita+One&family=Nunito+Sans:wght@400;700&family=Arimo:wght@400;500&family=Montserrat:wght@500&display=swap">
<style>
  :root {
    --ink: #111111;
    --white: #ffffff;
    --accent: #35a6d8;
    --button: #1a93cf;
    --body-text: #333333;
    --footer-bg: #000000;
    --rule: #3a3a3a;
  }
  * { box-sizing: border-box; margin: 0; padding: 0; }
  html, body { width: 1200px; height: 904px; overflow: hidden; background: var(--white); }
  .page { position: relative; width: 1200px; height: 904px; font-family: "Nunito Sans", sans-serif; }

  .hero {
    position: absolute; left: 0; top: 0; width: 1200px; height: 298px;
    background: linear-gradient(100deg, #3b4b60 0%, #c9d3dc 30%, #e8edf2 48%, #55657a 62%, #2e3a4e 75%, #a9b2bb 90%, #6b8fb0 100%);
  }
  .brand {
    position: absolute; font-family: "Montserrat", sans-serif; font-weight: 500; line-height: 1; white-space: nowrap;
  }
  .header-brand { left: 196px; top: 20px; color: var(--ink); font-size: 26px; letter-spacing: 0.5px; }
  .nav { position: absolute; top: 25px; left: 675px; display: flex; gap: 18px; }
  .nav a {
    font-family: "Nunito Sans", sans-serif; font-weight: 700; font-size: 11.5px;
    color: var(--white); text-decoration: none; letter-spacing: 0.2px;
  }
  .hero-title {
    position: absolute; left: 0; width: 1200px; top: 136px; text-align: center;
    font-family: "Lilita One", sans-serif; font-weight: 400; font-size: 48px; color: var(--white); letter-spacing: 1px;
  }

  .frame { position: absolute; left: 196px; top: 361px; width: 402px; height: 295px; border: 11px solid var(--accent); }
  .feature-photo {
    position: absolute; left: 225px; top: 388px; width: 404px; height: 240px;
    background: linear-gradient(90deg, #cfd2d0 0%, #4a4f5a 25%, #e7e2d8 50%, #f1efe9 65%, #2a3044 85%, #d9d7d1 100%);
    box-shadow: 0 0 6px rgba(53,166,216,0.25);
  }
  .feature-text { position: absolute; left: 657px; top: 414px; width: 346px; }
  .feature-text h2 { font-family: "Lilita One", sans-serif; font-weight: 400; font-size: 33px; color: var(--ink); letter-spacing: 0.5px; line-height: 40px; }
  .feature-text p { font-size: 10.6px; line-height: 17px; color: var(--body-text); margin-top: 12px; }
  .feature-text p + p { margin-top: 17px; }

  .footer { position: absolute; left: 0; top: 740px; width: 1200px; height: 164px; background: var(--footer-bg); color: var(--white); font-family: "Arimo", sans-serif; }
  .footer-brand { left: 196px; top: 46px; color: var(--white); font-size: 40px; }
  .footer-blurb { position: absolute; left: 446px; top: 35px; width: 154px; font-size: 9.6px; line-height: 12px; }
  .footer-blurb span { display: block; margin-bottom: 8px; }
  .footer-address { position: absolute; left: 628px; top: 35px; font-size: 9.6px; line-height: 12.2px; font-style: normal; }
  .newsletter { position: absolute; left: 782px; top: 36px; width: 220px; }
  .newsletter h3 { font-weight: 500; font-size: 14px; }
  .signup { display: flex; margin-top: 9px; height: 22px; }
  .signup .email { flex: 1; border-bottom: 1px solid var(--white); font-size: 8.5px; padding: 5px 1px 0; color: #dddddd; }
  .signup .subscribe { width: 64px; background: var(--button); font-size: 8.5px; font-weight: 500; text-align: center; line-height: 22px; }
  .footer-rule { position: absolute; left: 0; top: 123px; width: 1200px; height: 1px; background: var(--rule); }
  .copyright { position: absolute; left: 196px; top: 140px; font-size: 9.4px; }
  .legal { position: absolute; right: 198px; top: 140px; display: flex; gap: 21px; font-size: 9.4px; }
</style>
</head>
<body>
<div class="page">
  <header class="hero" role="img" aria-label="Photo of business people meeting in a bright office atrium">
    <div class="brand header-brand">VELBRIC</div>
    <nav class="nav">
      <a href="#">HOME</a><a href="#">ABOUT</a><a href="#">SERVICES</a><a href="#">PRODUCTS</a><a href="#">CONTACT</a>
    </nav>
    <h1 class="hero-title">SOLUTIONS</h1>
  </header>

  <section class="feature">
    <div class="frame"></div>
    <div class="feature-photo" role="img" aria-label="Photo of two colleagues shaking hands in an office"></div>
    <div class="feature-text">
      <h2>SMB CLIENT</h2>
      <p>Are you a small or medium sized business looking to begin your digital transformation journey through automation of simple and repetitive conversational workflows? Well, you’re in luck because we offer our tmPilot solution on a smaller scale for smaller clients.</p>
      <p>Please visit www.tmpilot.example for more information on how we can assist you through yourjourney! Or contact us at info@velbriclimited.example for a catered demo.</p>
    </div>
  </section>

  <footer class="footer">
    <div class="brand footer-brand">VELBRIC</div>
    <div class="footer-blurb">
      <span>Lorem ipsum dolor sit amet,</span>
      <span>consectetur adipiscing elit, sed do eiusmod tempor incididunt ut labore et dolore magna aliqua.</span>
    </div>
    <address class="footer-address">Velbric Ltd.<br>2150 Harlow Street,<br>Unit 7 &amp; 8<br>Brenford, ON<br>Canada K0X 1Z9</address>
    <div class="newsletter">
      <h3>Newsletter Sign Up</h3>
      <div class="signup"><span class="email">Email Address</span><span class="subscribe">Subscribe</span></div>
    </div>
    <div class="footer-rule"></div>
    <div class="copyright">© 2020 Velbric Limited. All Rights Reserved.</div>
    <div class="legal"><span>Terms Of Use</span><span>Privacy Policy</span></div>
  </footer>
</div>
</body>
</html>
```